Corwell Facilities Services Business Card.

We need a card for Corwell Facilities Services with a new look. We also have service and supply partners that we would like to have on the card. Lumacoat is a surface application company, Corwell Facilities is a facilities services business, Tavish Supply Co is a Facilities supply business, Pelvra is a product that we use that powers our business.

```html
<!DOCTYPE html>
<html lang="en">
<head>
<meta charset="utf-8">
<title>Corwell Facilities Services – Business Card</title>
<link rel="stylesheet" href="https://fonts.googleapis.com/css2?family=Montserrat:wght@500;600;700;800&family=Roboto:wght@400;500&display=swap">
<style>
  :root {
    --brand-blue: #1f6fbf;
    --brand-green: #3bb54a;
    --ink-dark: #1b2236;
    --partner-cyan: #36b3d9;
    --card-white: #ffffff;
    --page-bg: #e9ecef;
  }
  * { margin: 0; padding: 0; box-sizing: border-box; }
  html, body { width: 1200px; height: 913px; overflow: hidden; }
  body {
    background: var(--page-bg);
    position: relative;
    font-family: "Montserrat", sans-serif;
  }
  .card {
    position: absolute;
    width: 560px;
    height: 320px;
    background: var(--card-white);
    box-shadow: 0 6px 18px rgba(0,0,0,0.18);
    overflow: hidden;
  }
  .card--front { left: 80px; top: 70px; }
  .card--back { left: 560px; top: 520px; }

  /* Wordmark */
  .wordmark { display: flex; align-items: center; gap: 12px; color: var(--brand-blue); font-weight: 800; }
  .wordmark__dot { border-radius: 50%; background: var(--brand-blue); flex: none; }
  .wordmark__text { display: flex; flex-direction: column; line-height: 0.95; }
  .wordmark__name { letter-spacing: -1px; }

  .card--front .wordmark { position: absolute; left: 110px; top: 78px; }
  .card--front .wordmark__dot { width: 56px; height: 56px; }
  .card--front .wordmark__name { font-size: 78px; }
  .card--front .wordmark__tagline { font-size: 26px; margin-top: 4px; }

  .partners {
    position: absolute; left: 0; right: 0; top: 248px;
    display: flex; justify-content: center; align-items: flex-end; gap: 34px;
  }
  .partner { font-weight: 700; font-size: 18px; line-height: 1; }
  .partner--powered { display: flex; flex-direction: column; color: var(--ink-dark); }
  .partner--powered .partner__label { font-size: 9px; font-weight: 600; margin-bottom: 3px; }
  .partner--powered .partner__name { font-size: 20px; font-weight: 800; }
  .partner--supply { color: var(--brand-blue); font-size: 16px; }
  .partner--coat { color: var(--partner-cyan); font-size: 16px; }

  /* Back */
  .card--back .wordmark { position: absolute; left: 40px; top: 118px; gap: 8px; }
  .card--back .wordmark__dot { width: 34px; height: 34px; }
  .card--back .wordmark__name { font-size: 50px; }
  .card--back .wordmark__tagline { font-size: 16px; margin-top: 3px; }

  .divider { position: absolute; left: 282px; top: 46px; width: 2px; height: 170px; background: var(--brand-blue); }

  .contact { position: absolute; left: 300px; top: 44px; color: var(--brand-blue); }
  .contact__name { font-size: 22px; font-weight: 700; letter-spacing: 1px; line-height: 1.1; }
  .contact__title { font-family: "Roboto", sans-serif; font-size: 13px; color: var(--brand-green); letter-spacing: 1px; margin-top: 2px; }
  .contact__address { font-family: "Roboto", sans-serif; font-size: 12px; line-height: 1.35; margin-top: 12px; }
  .contact__list { list-style: none; margin-top: 10px; font-family: "Roboto", sans-serif; font-size: 15px; }
  .contact__item { display: flex; align-items: center; gap: 8px; line-height: 1.45; }
  .contact__icon { width: 14px; height: 14px; fill: var(--brand-blue); flex: none; }

  .base-band { position: absolute; left: 0; bottom: 0; width: 560px; height: 100px; }
</style>
</head>
<body>

<section class="card card--front" aria-label="Card front">
  <div class="wordmark">
    <span class="wordmark__dot"></span>
    <div class="wordmark__text">
      <span class="wordmark__name">Corwell</span>
      <span class="wordmark__tagline">Facilities Services</span>
    </div>
  </div>
  <div class="partners">
    <div class="partner partner--powered">
      <span class="partner__label">Powered by</span>
      <span class="partner__name">PELVRA</span>
    </div>
    <div class="partner partner--supply">TAVISH SUPPLY CO</div>
    <div class="partner partner--coat">LUMACOAT</div>
  </div>
</section>

<section class="card card--back" aria-label="Card back">
  <div class="wordmark">
    <span class="wordmark__dot"></span>
    <div class="wordmark__text">
      <span class="wordmark__name">Corwell</span>
      <span class="wordmark__tagline">Facilities Services</span>
    </div>
  </div>

  <div class="divider"></div>

  <div class="contact">
    <div class="contact__name">DANIEL ASHBY</div>
    <div class="contact__title">DIRECTOR</div>
    <div class="contact__address">48 Harlow Lane, Westbury,<br>(Harlow Station Exit B)</div>
    <ul class="contact__list">
      <li class="contact__item">
        <svg class="contact__icon" viewBox="0 0 24 24"><path d="M6.6 10.8a15 15 0 0 0 6.6 6.6l2.2-2.2a1 1 0 0 1 1-.25 11.4 11.4 0 0 0 3.6.57 1 1 0 0 1 1 1V20a1 1 0 0 1-1 1A17 17 0 0 1 3 4a1 1 0 0 1 1-1h3.5a1 1 0 0 1 1 1c0 1.25.2 2.45.57 3.6a1 1 0 0 1-.25 1z"/></svg>
        <span>555 010 2244</span>
      </li>
      <li class="contact__item">
        <svg class="contact__icon" viewBox="0 0 24 24"><path d="M2 5h20v14H2z M2 5l10 8 10-8" fill="none" stroke="#1f6fbf" stroke-width="2"/></svg>
        <span>info@corwellfs.com</span>
      </li>
      <li class="contact__item">
        <svg class="contact__icon" viewBox="0 0 24 24"><circle cx="12" cy="12" r="9" fill="none" stroke="#1f6fbf" stroke-width="2"/><path d="M3 12h18M12 3c3 3 3 15 0 18M12 3c-3 3-3 15 0 18" fill="none" stroke="#1f6fbf" stroke-width="1.6"/></svg>
        <span>www.corwellfs.com</span>
      </li>
    </ul>
  </div>

  <svg class="base-band" viewBox="0 0 560 100" preserveAspectRatio="none" aria-hidden="true">
    <path d="M0 70 L400 70 C430 70 440 50 460 30 C480 10 520 0 560 0 L560 100 L0 100 Z" fill="var(--brand-blue)"/>
    <path d="M410 70 C440 66 455 40 475 22 C495 6 525 0 560 0 L560 100 L410 100 Z" fill="var(--brand-green)"/>
    <path d="M400 70 C430 70 440 50 460 30 C475 16 495 8 520 4 C490 14 470 34 455 52 C445 64 430 70 410 72 Z" fill="#ffffff"/>
  </svg>
</section>

</body>
</html>
```